Business Card Design

6 piece Rock and Roll Cover band playing music from the 60's to present. We've got "The Wrens" as 2 lead vocalists singing anyone from the Humming Wires and Marrowgate to Copper moth ensemble and velvet ferrets through the The Pale Hinges. we play some bluesy country songs like those by the Quarry Belles and Delphine Harwick. We are based out of Camden, ME and are interested in venues that like to dance and party.
Our Design includes a western looking cartoon Pistol with smoke rolling out of the barrel as in - "nothing's hotter than a nine penny Lantern (stolen)" We like Grays and greens with some hints of yellow and white
Target Market(s)
ages 25-30
Industry/Entity Type
Business
Contact Information for Business Card
NINE PENNY LANTERN
facebook.com/9pennylanternharbor
ninepenny@ninepennylanternharbor.com

```html
<!DOCTYPE html>
<html lang="en">
<head>
<meta charset="utf-8">
<title>Nine Penny Lantern – Business Card</title>
<link rel="stylesheet" href="https://fonts.googleapis.com/css2?family=Stardos+Stencil:wght@700&family=Open+Sans:wght@400;600&display=swap">
<style>
  :root {
    --backdrop: #3b3a3c;
    --card: #2a302b;
    --card-edge: #1f2420;
    --red: #e8242b;
    --band-gray: #4a4b4c;
    --name-gray: #8e8f90;
    --text-light: #c9c9c9;
    --art-steel: #9fb4c4;
    --art-shadow: #5d6d7a;
  }
  html, body {
    margin: 0;
    width: 1200px;
    height: 1000px;
    overflow: hidden;
    background: var(--backdrop);
  }
  .canvas {
    position: relative;
    width: 1200px;
    height: 1000px;
  }
  .card {
    position: absolute;
    left: 320px;
    width: 560px;
    height: 320px;
    background: var(--card);
    box-shadow: 0 3px 0 var(--card-edge), 0 14px 30px rgba(0,0,0,.45);
    overflow: hidden;
  }
  .card--front { top: 130px; }
  .card--back { top: 550px; }

  .pistol-art {
    position: absolute;
    width: 180px;
    height: 150px;
    border-radius: 40% 50% 45% 35%;
    background: radial-gradient(ellipse at 45% 40%, var(--art-steel), var(--art-shadow) 70%, transparent 72%);
    z-index: 2;
  }
  .card--front .pistol-art { right: 40px; top: 18px; }
  .card--back .pistol-art { right: 30px; top: 14px; }

  .phone-band {
    position: absolute;
    left: 0; right: 0;
    top: 150px;
    height: 62px;
    background: var(--red);
    display: flex;
    align-items: center;
    padding-left: 36px;
    gap: 18px;
    font-family: "Open Sans", sans-serif;
    font-size: 22px;
    letter-spacing: 6px;
    color: var(--card);
    z-index: 1;
  }
  .phone-band svg { width: 20px; height: 20px; }

  .name-band {
    position: absolute;
    left: 0; right: 0;
    top: 104px;
    height: 76px;
    background: var(--band-gray);
    padding: 12px 0 0 30px;
    box-sizing: border-box;
    z-index: 1;
  }
  .name-band .band-name {
    font-family: "Stardos Stencil", sans-serif;
    font-weight: 700;
    font-size: 26px;
    line-height: 30px;
    letter-spacing: 2px;
    color: var(--red);
    margin: 0;
  }
  .name-band .tagline {
    font-family: "Open Sans", sans-serif;
    font-size: 11px;
    color: var(--text-light);
    margin: 6px 0 0 0;
  }
  .contacts {
    position: absolute;
    left: 30px;
    top: 196px;
    font-family: "Open Sans", sans-serif;
    font-size: 14px;
    color: var(--red);
    line-height: 26px;
  }
  .contact-row { display: flex; align-items: center; gap: 10px; }
  .contact-icon {
    width: 16px; height: 16px;
    background: var(--name-gray);
    display: inline-block;
  }
  .footer-band {
    position: absolute;
    left: 0; right: 0; bottom: 0;
    height: 58px;
    background: var(--red);
    display: flex;
    align-items: center;
    padding-left: 30px;
    font-family: "Stardos Stencil", sans-serif;
    font-weight: 700;
    font-size: 28px;
    letter-spacing: 3px;
    color: var(--name-gray);
  }
</style>
</head>
<body>
<main class="canvas">
  <section class="card card--front">
    <div class="pistol-art" role="img" aria-label="Illustration of a western cartoon pistol with smoke from the barrel"></div>
    <div class="phone-band">
      <svg viewBox="0 0 24 24" aria-hidden="true"><path fill="#2a302b" d="M6.6 10.8a15 15 0 0 0 6.6 6.6l2.2-2.2c.3-.3.7-.4 1-.2 1.1.4 2.3.6 3.6.6.6 0 1 .4 1 1V20c0 .6-.4 1-1 1A17 17 0 0 1 3 4c0-.6.4-1 1-1h3.5c.6 0 1 .4 1 1 0 1.3.2 2.5.6 3.6.1.3 0 .7-.2 1z"/></svg>
      <span class="phone-number">123-456-789</span>
    </div>
  </section>

  <section class="card card--back">
    <div class="pistol-art" role="img" aria-label="Illustration of a western cartoon pistol with smoke from the barrel"></div>
    <div class="name-band">
      <h1 class="band-name">NINE PENNY LANTERN</h1>
      <p class="tagline">Nothing's hotter than a nine penny Lantern</p>
    </div>
    <div class="contacts">
      <div class="contact-row"><span class="contact-icon"></span>facebook.com/9pennylanternharbor</div>
      <div class="contact-row"><span class="contact-icon"></span>ninepenny@ninepennylanternharbor.com</div>
    </div>
    <div class="footer-band">NINE PENNY LANTERN</div>
  </section>
</main>
</body>
</html>
```